Health care technology software systems

We have a solid logo. We have company colors that will need to be used as well. We just need a great business card design. We sell to health plans but want to be modern
Updates

Need extra days to review

Target Market(s)

Health technology sector selling into Health Plans

Industry/Entity Type

Health Care Technology

Contact Information for Business Card

Name, title, address, phone number, email

Requirements
Must have
• Use of Kembrata corporate colors - Uploaded w/ our logos

```html
<!DOCTYPE html>
<html lang="en">
<head>
<meta charset="utf-8">
<title>Kembrata — Business Card</title>
<link rel="stylesheet" href="https://fonts.googleapis.com/css2?family=Open+Sans:wght@300;400;700&display=swap">
<style>
  :root {
    --backdrop: #e4e4e4;
    --card-dark: #383a38;
    --card-light: #f4f4f4;
    --band: #363836;
    --ink: #3a3a3a;
    --ink-soft: #3c3c3c;
    --brand-blue: #1a9ad6;
    --brand-green: #7ab648;
    --white: #ffffff;
  }
  * { margin: 0; padding: 0; box-sizing: border-box; }
  html, body {
    width: 1200px; height: 960px; overflow: hidden;
    background: var(--backdrop);
    font-family: "Open Sans", sans-serif;
  }
  .card {
    position: absolute; left: 307px;
    width: 596px; height: 340px;
    border-radius: 18px; overflow: hidden;
  }
  .card--front { top: 115px; background: var(--card-dark); }
  .card--back { top: 508px; background: var(--card-light); }

  .front-pattern {
    position: absolute; inset: 0;
    background: linear-gradient(100deg, #6e6e6e 0%, #4a4b4a 40%, #232423 70%, #111211 100%);
  }
  .brand {
    position: absolute; display: flex; align-items: center;
  }
  .brand__dot {
    border-radius: 50%; background: var(--brand-blue); flex: none;
  }
  .brand__name {
    font-weight: 300; line-height: 1; letter-spacing: 1px;
  }
  .card--front .brand { left: 138px; top: 142px; }
  .card--front .brand__dot { width: 56px; height: 56px; margin-right: 22px; }
  .card--front .brand__name { font-size: 58px; color: var(--white); }

  .back-band {
    position: absolute; left: 0; top: 0; bottom: 0; width: 67px;
    background: var(--band);
  }
  .back-decor {
    position: absolute; left: 340px; top: 110px; width: 300px; height: 300px;
    border-radius: 50%;
    background: radial-gradient(circle, rgba(244,244,244,1) 34%, rgba(214,228,238,0.9) 36%, rgba(224,234,214,0.7) 60%, rgba(244,244,244,0) 72%);
  }
  .card--back .brand { left: 32px; top: 38px; }
  .card--back .brand__dot {
    width: 66px; height: 66px; margin-right: 24px;
    border: 4px solid var(--white);
  }
  .card--back .brand__name { font-size: 58px; color: var(--ink); }

  .contact {
    position: absolute; left: 126px; top: 138px;
    color: var(--ink-soft); font-size: 14.5px; line-height: 20px;
  }
  .contact__name { color: var(--brand-blue); font-weight: 700; font-size: 18.5px; line-height: 24px; }
  .contact__title { margin-bottom: 22px; }
  .contact__address { margin-bottom: 8px; }
  .contact__row { display: flex; align-items: center; gap: 5px; }
  .contact__row svg { width: 13px; height: 13px; flex: none; }
</style>
</head>
<body>

<section class="card card--front" aria-label="Card front">
  <div class="front-pattern" role="img" aria-label="Repeating grid of brand symbols fading from grey to black"></div>
  <div class="brand">
    <span class="brand__dot"></span>
    <span class="brand__name">kembrata</span>
  </div>
</section>

<section class="card card--back" aria-label="Card back">
  <div class="back-band"></div>
  <div class="back-decor" role="img" aria-label="Faint large brand symbol in soft green and blue"></div>
  <div class="brand">
    <span class="brand__dot"></span>
    <span class="brand__name">kembrata</span>
  </div>
  <div class="contact">
    <p class="contact__name">Daniel Whitford</p>
    <p class="contact__title">President</p>
    <p class="contact__address">2450 NE ALDER ST 204<br>Salem, Oregon 97301</p>
    <p class="contact__row">
      <svg viewBox="0 0 16 16" aria-hidden="true"><path fill="var(--brand-green)" d="M3.5 1.5l2.5 0 1 3.5-1.6 1.2a9 9 0 0 0 4.4 4.4L11 9l3.5 1v2.5c0 1-.8 1.8-1.8 1.8C7 14.3 1.7 9 1.7 3.3c0-1 .8-1.8 1.8-1.8z"/></svg>
      (555) 318-2046
    </p>
    <p class="contact__row">
      <svg viewBox="0 0 16 16" aria-hidden="true"><rect x="1.5" y="3.5" width="13" height="9" fill="none" stroke="var(--brand-green)" stroke-width="1.6"/><path d="M1.5 3.5l6.5 5 6.5-5" fill="none" stroke="var(--brand-green)" stroke-width="1.6"/></svg>
      daniel@kembrata.com
    </p>
    <p class="contact__row">
      <svg viewBox="0 0 16 16" aria-hidden="true"><g fill="none" stroke="var(--brand-green)" stroke-width="1.3"><circle cx="8" cy="8" r="6.3"/><ellipse cx="8" cy="8" rx="2.8" ry="6.3"/><path d="M1.7 8h12.6M2.8 4.8h10.4M2.8 11.2h10.4"/></g></svg>
      www.kembrata.com
    </p>
  </div>
</section>

</body>
</html>
```